FILE SETUP - BENEFITS FOR DOGS / CATS

hello ,

looking to set up a file for the printer in regards to benefits for dogs and benefits for cats.

Two Sided. Front and Back.

```html
<!DOCTYPE html>
<html lang="en">
<head>
<meta charset="utf-8">
<title>Benefits for Cats</title>
<link href="https://fonts.googleapis.com/css2?family=Montserrat:wght@300;800&family=Anton&family=Open+Sans:wght@400&family=PT+Sans+Narrow:wght@700&display=swap" rel="stylesheet">
<style>
  :root {
    --ink: #0b0b0b;
    --sky: #27a9e1;
    --rose: #ec82b1;
    --green: #2bb673;
    --royal: #1c75bc;
    --red: #ef4136;
    --orange: #f7941d;
    --navy: #2e3192;
    --paper: #ffffff;
    --paw-grey: #e4e2ec;
    --paw-mint: #e3f3ef;
    --paw-pink: #f8d3e2;
    --paw-violet: rgba(150, 110, 170, 0.35);
  }
  html, body {
    margin: 0;
    padding: 0;
    width: 927px;
    height: 1200px;
    overflow: hidden;
    background: var(--paper);
  }
  .poster {
    position: relative;
    width: 990px;
    height: 1282px;
    transform: scale(0.93636);
    transform-origin: 0 0;
    overflow: hidden;
    background: var(--paper);
  }
  .backdrop, .paws-front { position: absolute; inset: 0; }
  .paws-front { pointer-events: none; }
  .title-main {
    position: absolute;
    left: 136px; top: 70px;
    margin: 0;
    font-family: "Montserrat", sans-serif;
    font-weight: 800;
    font-size: 146px;
    line-height: 1;
    color: var(--ink);
    letter-spacing: -3px;
    transform: scaleX(0.86);
    transform-origin: 0 0;
    white-space: nowrap;
  }
  .title-for {
    position: absolute;
    left: 144px; top: 223px;
    font-family: "Montserrat", sans-serif;
    font-weight: 300;
    font-size: 72px;
    line-height: 1;
    color: var(--ink);
  }
  .title-subject {
    position: absolute;
    left: 318px; top: 199px;
    font-family: "Anton", sans-serif;
    font-size: 245px;
    line-height: 1;
    color: var(--rose);
    letter-spacing: 2px;
    transform: scaleX(1.15);
    transform-origin: 0 0;
  }
  .line {
    position: absolute;
    white-space: nowrap;
    transform: translateX(-50%);
    line-height: 1;
  }
  .label {
    font-family: "Open Sans", sans-serif;
    font-weight: 400;
    font-size: 27px;
    color: var(--ink);
    letter-spacing: -0.5px;
  }
  .benefit {
    font-family: "PT Sans Narrow", sans-serif;
    font-weight: 700;
    font-size: 60px;
    letter-spacing: -1px;
  }
  .benefit .small { font-size: 44px; }
  .c-sky { color: var(--sky); }
  .c-rose { color: var(--rose); }
  .c-green { color: var(--green); }
  .c-royal { color: var(--royal); }
  .c-red { color: var(--red); }
  .c-orange { color: var(--orange); }
  .c-navy { color: var(--navy); }
  .kitten {
    position: absolute;
    left: 0; top: 680px;
    width: 440px; height: 602px;
  }
</style>
</head>
<body>
<main class="poster">
  <svg class="backdrop" viewBox="0 0 990 1282" width="990" height="1282" aria-hidden="true">
    <path d="M690 0 C640 40 560 45 450 60 C320 80 200 120 110 190 C60 230 30 260 0 275 L0 0 Z" fill="var(--rose)"/>
    <path d="M665 0 C630 25 560 30 450 42 C320 60 190 100 100 170 C55 205 25 235 0 250 L0 0 Z" fill="var(--sky)"/>
    <path d="M0 262 C80 255 120 300 150 360 C185 430 215 500 260 560 C300 610 325 650 330 720 L330 1282 L0 1282 Z" fill="var(--sky)"/>
    <path d="M0 255 C70 250 105 295 135 355 C170 425 200 495 245 555 C285 605 312 650 316 720 L316 1282 L0 1282 Z" fill="var(--rose)"/>
  </svg>

  <svg class="backdrop" viewBox="0 0 990 1282" width="990" height="1282" role="img" aria-label="Soft paw print decorations">
    <circle cx="560" cy="62" r="28" fill="var(--paw-pink)" opacity="0.6"/>
    <circle cx="885" cy="150" r="55" fill="var(--paw-grey)"/>
    <circle cx="225" cy="385" r="52" fill="var(--paw-mint)"/>
    <circle cx="660" cy="330" r="50" fill="var(--paw-mint)"/>
    <circle cx="315" cy="505" r="50" fill="var(--paw-pink)"/>
  </svg>

  <h1 class="title-main">BENEFITS</h1>
  <div class="title-for">FOR</div>
  <div class="title-subject">CATS</div>

  <svg class="paws-front" viewBox="0 0 990 1282" width="990" height="1282" role="img" aria-label="Faint paw print over the title">
    <circle cx="372" cy="238" r="44" fill="var(--paw-violet)"/>
  </svg>

  <div class="line label" style="left:548px; top:474px;">CATS ARE GREAT</div>
  <div class="line benefit c-sky" style="left:553px; top:499px;">COMPANIONS</div>

  <div class="line label" style="left:841px; top:498px;">CATS REDUCE</div>
  <div class="line benefit c-rose" style="left:836px; top:523px;">LONELINESS</div>

  <div class="line label" style="left:545px; top:579px;">CATS TEACH YOU TO</div>
  <div class="line benefit c-green" style="left:586px; top:606px;">LOVE UNCONDITIONALLY</div>

  <div class="line label" style="left:704px; top:674px;">CATS IMPROVE YOUR</div>
  <div class="line benefit c-royal" style="left:703px; top:700px;">PHYSICAL HEALTH</div>

  <div class="line label" style="left:685px; top:780px;">CATS RELIEVE</div>
  <div class="line benefit c-red" style="left:675px; top:806px;">STRESS <span class="small">AND</span> ANXIETY</div>

  <div class="line label" style="left:687px; top:875px;">CATS ARE GOOD FOR YOUR</div>
  <div class="line benefit c-orange" style="left:688px; top:902px;">MENTAL HEALTH,</div>
  <div class="line benefit c-orange" style="left:695px; top:952px;"><span class="small">AND</span> YOUR CHILDREN’S</div>

  <div class="line label" style="left:655px; top:1023px;">CATS GIVE YOU</div>
  <div class="line benefit c-red" style="left:685px; top:1049px;">A SENSE OF PURPOSE</div>

  <div class="line label" style="left:648px; top:1128px;">CATS CAN HELP YOU</div>
  <div class="line benefit c-navy" style="left:731px; top:1156px;">MEET PEOPLE <span class="small">AND</span></div>
  <div class="line benefit c-navy" style="left:762px; top:1209px;">MAKE FRIENDS</div>

  <svg class="kitten" viewBox="0 0 440 602" width="440" height="602" role="img" aria-label="Illustration of a sitting calico kitten in white, orange and dark grey">
    <defs>
      <linearGradient id="kittenTone" x1="0" y1="0" x2="1" y2="1">
        <stop offset="0" stop-color="#5a5250"/>
        <stop offset="0.35" stop-color="#f4f1f2"/>
        <stop offset="0.7" stop-color="#f7b267"/>
        <stop offset="1" stop-color="#f2e8e4"/>
      </linearGradient>
    </defs>
    <ellipse cx="215" cy="580" rx="215" ry="22" fill="#e3cfc0"/>
    <rect x="15" y="10" width="415" height="570" rx="120" fill="url(#kittenTone)"/>
  </svg>
</main>
</body>
</html>
```